Picture Ads

We need some banner ads for our home business opportunity, we are evolving from text to picture ads. I have added some examples of what other distributors are using. We are looking for something really eye catching with some good key words and nice bright colours and to include our photo (attached)
Key words to include:
Booming online business
Personal Development and Leadership Industry
Earn an executive income from home
Simple 3 step system
Make up to $5,000 per sale
Not MLM
The size needs to be: 1000 x 35 pixels
13.9 x 4.75 Inches
35.3 x 11.1 cm
I think different platforms accept different sizes, not too familiar with it yet, any guidance welcome. I've clicked project for 2 days if that is to prioritise the order?
Many thanks,
Maren

Industry/Entity Type

Business

```html
<!DOCTYPE html>
<html lang="en">
<head>
<meta charset="utf-8">
<title>Booming Online Business Banner</title>
<link href="https://fonts.googleapis.com/css2?family=Anton&family=Archivo+Black&family=Archivo+Narrow:wght@500;700&display=swap" rel="stylesheet">
<style>
  :root {
    --purple: #8e2bd6;
    --purple-deep: #6a1fa8;
    --magenta: #f21bd6;
    --pink-light: #fbd3f6;
    --pink-mid: #f2a6ea;
    --lilac: #d47ae8;
    --ink: #111111;
    --white: #ffffff;
  }
  html, body {
    margin: 0;
    padding: 0;
    width: 1200px;
    height: 378px;
    overflow: hidden;
    background: var(--white);
  }
  .banner {
    position: relative;
    width: 1200px;
    height: 378px;
    overflow: hidden;
  }
  .banner svg { display: block; }
  .headline-font { font-family: "Anton", "Impact", sans-serif; }
  .heavy-font { font-family: "Archivo Black", "Arial Black", sans-serif; }
  .narrow-font { font-family: "Archivo Narrow", "Arial Narrow", sans-serif; }
</style>
</head>
<body>
<div class="banner">
  <svg width="1200" height="378" viewBox="0 0 1200 378" xmlns="http://www.w3.org/2000/svg">
    <defs>
      <linearGradient id="bg-wash" x1="0" y1="0" x2="1" y2="1">
        <stop offset="0" stop-color="#fde6fb"/>
        <stop offset="0.45" stop-color="#f6b9ef"/>
        <stop offset="1" stop-color="#e08be6"/>
      </linearGradient>
      <linearGradient id="photo-tone" x1="0" y1="0" x2="1" y2="1">
        <stop offset="0" stop-color="#6b4a3a"/>
        <stop offset="0.5" stop-color="#c98a6a"/>
        <stop offset="1" stop-color="#3a2420"/>
      </linearGradient>
      <radialGradient id="dot-wash" cx="0.5" cy="0.5" r="0.6">
        <stop offset="0" stop-color="#ffffff" stop-opacity="0.75"/>
        <stop offset="1" stop-color="#ffffff" stop-opacity="0"/>
      </radialGradient>
    </defs>

    <!-- background field -->
    <rect class="background" x="340" y="0" width="860" height="378" fill="url(#bg-wash)"/>
    <ellipse class="soft-glow" cx="560" cy="250" rx="210" ry="120" fill="url(#dot-wash)"/>

    <!-- swooshes -->
    <path class="swoosh" d="M560 378 C760 250 950 170 1200 120 L1200 200 C980 230 780 300 680 378 Z" fill="#ffffff" opacity="0.55"/>
    <path class="swoosh" d="M700 378 C860 300 1020 250 1200 230 L1200 378 Z" fill="var(--lilac)" opacity="0.55"/>
    <path class="swoosh" d="M1000 0 C1080 60 1140 80 1200 90 L1200 0 Z" fill="#ffffff" opacity="0.5"/>

    <!-- photo area -->
    <rect class="photo" x="0" y="0" width="348" height="378" fill="url(#photo-tone)" role="img" aria-label="Photo of two smiling women, the business owners"/>

    <!-- step system bar -->
    <rect class="step-bar" x="0" y="318" width="342" height="60" fill="var(--purple)"/>
    <text class="step-text heavy-font" x="171" y="358" text-anchor="middle" font-size="25" fill="var(--white)">Simple <tspan font-size="40">3</tspan> step system</text>

    <!-- free info tab -->
    <path class="info-tab" d="M640 0 H906 V32 Q906 48 890 48 H656 Q640 48 640 32 Z" fill="var(--purple)"/>
    <text class="info-text narrow-font" x="773" y="34" text-anchor="middle" font-size="24" font-weight="700" fill="var(--white)">Click <tspan font-weight="500">here for</tspan> Free Info</text>

    <!-- headline -->
    <text class="headline headline-font" x="772" y="150" text-anchor="middle" font-size="92" textLength="770" lengthAdjust="spacingAndGlyphs"
          fill="var(--white)" stroke="var(--purple)" stroke-width="14" stroke-linejoin="round" paint-order="stroke">Booming Online Business</text>

    <!-- industry line -->
    <text class="industry heavy-font" x="782" y="210" text-anchor="middle" font-size="33" textLength="756" lengthAdjust="spacingAndGlyphs" stroke="var(--white)" stroke-width="4" paint-order="stroke" stroke-linejoin="round">
      <tspan fill="var(--ink)">Personal </tspan><tspan fill="var(--magenta)" class="headline-font">Development</tspan><tspan fill="var(--ink)"> and </tspan><tspan fill="var(--magenta)" class="headline-font">Leadership</tspan><tspan fill="var(--ink)"> Industry</tspan>
    </text>

    <!-- income line -->
    <text class="income" x="722" y="260" text-anchor="middle" textLength="620" lengthAdjust="spacingAndGlyphs" stroke="var(--white)" stroke-width="4" paint-order="stroke" stroke-linejoin="round">
      <tspan class="headline-font" font-size="54" fill="var(--magenta)">Earn </tspan><tspan class="narrow-font" font-size="30" fill="var(--ink)">an executive </tspan><tspan class="headline-font" font-size="54" fill="var(--magenta)">Income </tspan><tspan class="narrow-font" font-size="30" fill="var(--ink)">from </tspan><tspan class="headline-font" font-size="54" fill="var(--magenta)">home</tspan>
    </text>

    <!-- sale line -->
    <text class="sale narrow-font" x="713" y="335" text-anchor="middle" textLength="600" lengthAdjust="spacingAndGlyphs" font-weight="500">
      <tspan font-size="52" fill="var(--ink)">Make up to </tspan><tspan class="headline-font" font-size="70" fill="var(--white)" stroke="var(--purple)" stroke-width="12" stroke-linejoin="round" paint-order="stroke">$5,000</tspan><tspan font-size="52" fill="var(--ink)"> per sale</tspan>
    </text>

    <!-- not MLM badge -->
    <circle class="badge" cx="1108" cy="300" r="68" fill="var(--purple)"/>
    <g class="badge-text headline-font" fill="var(--white)" stroke="var(--ink)" stroke-width="3" paint-order="stroke" text-anchor="middle">
      <text x="1102" y="290" font-size="40">Not</text>
      <text x="1108" y="340" font-size="50">MLM</text>
    </g>
  </svg>
</div>
</body>
</html>
```